Purrline Fest Ticket Card Design

We’re looking to create a complimentary “ticket” card for Purrline Fest that can be handed out physically. We host an event for cat lovers. The card should feel special and collectible. Size will be a standard business card (3.5" x 2") Orientation is open to designer recommendation. This ticket will be used as a complimentary entry pass for select guests, partners, & giveaways. Key elements to Include are the Purrline Fest logo (provided), the words “Complimentary Ticket” or similar wording (open to creative phrasing and cat puns) A blank space for the Event date (to be written in) & Ticket number (to be written in) . Event Name is always "Purrline Bazaar & Rescue Gala". We want the ticket to feel clean & modern but slightly playful with a cat-inspired touch (think clever, not kitschy). Could include a subtle cat motif or texture (e.g., whisker lines, paw detail, soft patterning) Open to unique layout ideas that still leave clear writing space. Avoid overcrowding of elements. Ticket should also have fine print "This ticket is not redeemable for cash and cannot be combined with any other offers or discounts, can only be used for the date indicated"

Target Market(s)

Women

Industry/Entity Type

pets

Colors
6B429C
8869AF
B7A5CE
E3DAEB
F3F0F8

Requirements
Must have
• Purrline Fest Logo & words around complimentary ticket as well as the fine print
Nice to have
• cat-inspired touch (think clever, not kitschy). Could include a subtle cat motif or texture (e.g., whisker lines, paw detail, soft patterning)
Should not have
• should not look cartoony

```html
<!DOCTYPE html>
<html lang="en">
<head>
<meta charset="utf-8">
<title>Purrline Fest – Complimentary Ticket</title>
<link rel="stylesheet" href="https://fonts.googleapis.com/css2?family=Crimson+Pro:wght@400;500&family=Mulish:wght@800;900&display=swap">
<style>
  :root {
    --stage: #1a1a1c;
    --header: #7b6b9f;
    --header-stripe: #9b8cbd;
    --body: #cbc0df;
    --ink: #6e6192;
    --ink-soft: #6a5e86;
    --whisker: #8a7caf;
    --field: #efe9f5;
    --white: #ffffff;
  }
  * { margin: 0; padding: 0; box-sizing: border-box; }
  html, body { width: 1200px; height: 800px; overflow: hidden; background: var(--stage); }
  .ticket {
    position: absolute; left: 40px; top: 80px;
    width: 1120px; height: 640px;
    border-radius: 24px; overflow: hidden;
    background: var(--body);
  }
  .ticket__header {
    position: absolute; left: 0; top: 0; width: 100%; height: 162px;
    background: var(--header);
  }
  .ticket__stripe {
    position: absolute; left: 0; top: 162px; width: 100%; height: 26px;
    background: var(--header-stripe);
  }
  .brand {
    position: absolute; left: 34px; top: 44px;
    font-family: "Mulish", sans-serif; font-weight: 900;
    font-size: 46px; line-height: 1; color: var(--white);
    letter-spacing: 1px;
  }
  .event-name {
    position: absolute; left: 0; width: 100%; top: 218px;
    text-align: center;
    font-family: "Crimson Pro", serif; font-weight: 500;
    font-size: 40px; line-height: 50px; color: var(--ink);
  }
  .pass-title {
    position: absolute; left: 0; width: 100%; top: 276px;
    text-align: center;
    font-family: "Mulish", sans-serif; font-weight: 900;
    font-size: 54px; line-height: 68px; letter-spacing: 1.5px; color: var(--ink);
  }
  .whiskers { position: absolute; left: 0; top: 276px; width: 1120px; height: 110px; }
  .pass-subtitle {
    position: absolute; left: 0; width: 100%; top: 350px;
    text-align: center;
    font-family: "Crimson Pro", serif; font-weight: 500;
    font-size: 34px; line-height: 44px; color: var(--ink);
  }
  .field {
    position: absolute; top: 420px; height: 86px;
    background: var(--field); border-radius: 10px;
    font-family: "Crimson Pro", serif; font-weight: 500;
    font-size: 34px; line-height: 44px; color: var(--ink);
    padding: 18px 0 0 36px;
  }
  .field--date { left: 98px; width: 454px; }
  .field--number { left: 571px; width: 453px; }
  .fine-print {
    position: absolute; left: 53px; top: 538px; width: 790px;
    font-family: "Crimson Pro", serif; font-size: 20px; line-height: 29px;
    color: var(--ink-soft);
  }
</style>
</head>
<body>
  <div class="ticket">
    <div class="ticket__header" role="img" aria-label="Soft tonal pattern of cat doodles and paw prints"></div>
    <div class="ticket__stripe"></div>
    <div class="brand">Purrline Fest</div>

    <div class="event-name">Purrline Bazaar &amp; Rescue Gala</div>

    <svg class="whiskers" viewBox="0 0 1120 110" aria-hidden="true">
      <g stroke="var(--whisker)" stroke-width="2.5" stroke-linecap="round" fill="none">
        <line x1="180" y1="14" x2="292" y2="38"/>
        <line x1="172" y1="50" x2="290" y2="54"/>
        <line x1="186" y1="98" x2="292" y2="70"/>
        <line x1="940" y1="14" x2="828" y2="38"/>
        <line x1="948" y1="50" x2="830" y2="54"/>
        <line x1="934" y1="98" x2="828" y2="70"/>
      </g>
    </svg>
    <div class="pass-title">PAWSOME PASS!</div>
    <div class="pass-subtitle">Complimentary Entry</div>

    <div class="field field--date">Event Date</div>
    <div class="field field--number">Ticket No.</div>

    <p class="fine-print">This ticket is not redeemable for cash and connot be combined with any other offers or discounts, can only be used for the date indicated.</p>
  </div>
</body>
</html>
```